Plakat-Design zum Thema Personalabteilung
sehr zufrieden, Änderungen wurden schnell umgesetzt und Kommunikation war sehr gut
Zielgruppe
Morvena Software hat sich zum Ziel gesetzt, kleinen und mittleren Unternehmen über das Web schnell einsetzbare Lösungen zur Verfügung zu stellen, die ohne große Projektkosten direkt von der Personalabteilung genutzt werden können.
Frauen mittleren Alters in der Personalabteilung.
Aufgabenstellung
Formatvorgaben siehe Dokument 'Druckdatenblatt_Grossplakat'.
Wie haben uns 2 Designvorschläge überlegt. Bitte wählen Sie mindestens einen Vorschlag oder machen Sie zu jedem Design einen Entwurf.
Vorschlag 1:
Variante 1:
Dicker ekliger Chef
Sprechblase 1: meine Tussi in der Personalabteilung arbeitet 24/7 für mich
Sprechblase 2: und das völlig kostenfrei
stabwerkel.net
Footer mit: Luxemburg – Frankfurt – Leipzig/Halle – Wien
Variante 2:
Headline: Neues aus der Personalabteilung
Sprechblase 1: meine Tussi arbeitet 24/7 für mich
Vorschlag 2:
Tussi (Avatar)
Sprechblase: Ich arbeite 24/7 für meinen Chef, völlig kostenfrei und ich liebe es
kanzleigrund.cloud

```html
<!DOCTYPE html>
<html lang="de">
<head>
<meta charset="utf-8">
<title>Neues aus der Personalabteilung – Plakat</title>
<link href="https://fonts.googleapis.com/css2?family=Bangers&family=Patrick+Hand&family=Delius&display=swap" rel="stylesheet">
<style>
  :root {
    --page-bg: #ffffff;
    --signal-yellow: #ffec00;
    --ink: #111111;
    --magenta: #e6168f;
    --leaf-green: #5bb336;
    --photo-light: #c9cbcd;
    --photo-mid: #9a9c9f;
    --photo-dark: #4b4c4e;
    --white: #ffffff;
  }
  html, body {
    margin: 0;
    width: 1200px;
    height: 982px;
    overflow: hidden;
    background: var(--page-bg);
  }
  .poster {
    position: absolute;
    left: 30px;
    top: 94px;
    width: 1140px;
    height: 794px;
    overflow: hidden;
  }
  .poster__header {
    position: absolute;
    left: 0; top: 0;
    width: 100%;
    height: 101px;
    background: var(--signal-yellow);
    display: flex;
    align-items: center;
    justify-content: center;
  }
  .poster__headline {
    margin: 0;
    font-family: "Bangers", "Impact", sans-serif;
    font-size: 60px;
    letter-spacing: 2px;
    color: var(--ink);
    font-weight: 400;
    transform: skewX(-6deg);
    padding-top: 8px;
  }
  .poster__photo {
    position: absolute;
    left: 0; top: 101px;
    width: 100%;
    height: 693px;
    background:
      radial-gradient(ellipse 30% 45% at 57% 38%, #b08a76 0%, rgba(176,138,118,0) 70%),
      radial-gradient(ellipse 55% 40% at 55% 100%, var(--photo-dark) 0%, rgba(75,76,78,0) 80%),
      linear-gradient(180deg, var(--photo-light) 0%, var(--photo-mid) 100%);
  }
  .bubble {
    position: absolute;
  }
  .bubble svg { position: absolute; left: 0; top: 0; overflow: visible; }
  .bubble__text {
    position: absolute;
    margin: 0;
    font-family: "Patrick Hand", "Comic Sans MS", cursive;
    color: var(--white);
    text-transform: uppercase;
    text-align: center;
    line-height: 1.15;
  }
  .bubble--pink {
    left: 86px; top: 126px;
    width: 336px; height: 222px;
  }
  .bubble--pink .bubble__text {
    left: 20px; top: 28px;
    width: 290px;
    font-size: 26px;
    transform: rotate(-8deg);
  }
  .bubble--green {
    left: 784px; top: 152px;
    width: 216px; height: 150px;
  }
  .bubble--green .bubble__text {
    left: 14px; top: 22px;
    width: 190px;
    font-size: 25px;
    transform: rotate(4deg);
  }
  .poster__locations {
    position: absolute;
    right: 47px; top: 548px;
    margin: 0;
    font-family: "Delius", "Trebuchet MS", sans-serif;
    font-size: 19px;
    line-height: 1.55;
    text-align: right;
    color: var(--ink);
  }
  .poster__url {
    position: absolute;
    left: 369px; top: 708px;
    width: 404px; height: 86px;
    background: var(--signal-yellow);
    display: flex;
    align-items: center;
    justify-content: center;
    font-family: "Bangers", "Impact", sans-serif;
    font-size: 42px;
    letter-spacing: 2px;
    color: var(--ink);
  }
</style>
</head>
<body>
  <main class="poster">
    <header class="poster__header">
      <h1 class="poster__headline">NEUES AUS DER PERSONALABTEILUNG</h1>
    </header>

    <div class="poster__photo" role="img" aria-label="Foto: übergewichtiger Chef mit Glatze, Schnurrbart und Zigarre, in Weste und Krawatte, vor grauem Hintergrund"></div>

    <div class="bubble bubble--pink">
      <svg width="336" height="222" viewBox="0 0 336 222" aria-hidden="true">
        <path d="M168 14 C265 8 330 40 318 96 C308 150 235 176 162 180 L140 208 L132 182 C60 182 4 158 12 108 C20 52 80 18 168 14 Z"
              fill="var(--magenta)" stroke="#222" stroke-width="2.5" transform="rotate(-6 168 110)"/>
        <path d="M46 190 Q70 200 96 196 M56 204 Q80 210 104 206" fill="none" stroke="#222" stroke-width="2"/>
      </svg>
      <p class="bubble__text">Meine Tussi in<br>der Personalabteilung<br>arbeitet 24/7<br>für mich!</p>
    </div>

    <div class="bubble bubble--green">
      <svg width="216" height="150" viewBox="0 0 216 150" aria-hidden="true">
        <path d="M20 8 L200 18 Q210 19 209 30 L203 112 Q202 122 192 122 L66 118 L40 140 L44 116 L18 114 Q8 113 8 103 L10 18 Q10 8 20 8 Z"
              fill="var(--leaf-green)" stroke="#222" stroke-width="2.5"/>
        <path d="M14 130 Q8 140 14 148 M6 126 Q0 138 6 146" fill="none" stroke="#222" stroke-width="2"/>
      </svg>
      <p class="bubble__text">Und das<br>völlig<br>kostenfrei!</p>
    </div>

    <p class="poster__locations">Luxemburg - Frankfurt<br>Leipzig/Halle - Wien</p>

    <div class="poster__url">STABWERKEL.NET</div>
  </main>
</body>
</html>
```